Stationary for New Company

We need stationary designed for a new company. Details of the required stationary is attached.

The final version should be trendy, clean... only 2 colours (green + grey/black) and professional.

#1: Business Cards (design on 2 sides)
#2: Letterhead (word format)
#3: Cover Page and back cover for proposals
#4: Envelopes,
#5: Thank You card,
#6: Presentation Folder,
#7: Email signatures template (sample attached in word document)

Logo is attached. Logo can be reversed out (will attach once available). Logo can be stacked or horizontal (provided as horizontal).

Files need to be provided in ai + png format.

Target Market(s)

Business owners. More affluent.

Industry/Entity Type

Business

Requirements
Must have
• See brief

Font: Calibri
Should not have
• Photographs / stock photos

```html
<!DOCTYPE html>
<html lang="en">
<head>
<meta charset="utf-8">
<title>Parkline Insurance Brokers – Business Cards</title>
<link href="https://fonts.googleapis.com/css2?family=Open+Sans:wght@400;600;700&display=swap" rel="stylesheet">
<style>
  :root {
    --green: #6a9a2e;
    --green-faint: #dfe4cf;
    --charcoal: #3c3f44;
    --grey: #6d7075;
    --rule: #c9cacc;
    --card: #f4f4f2;
    --backdrop: #e3e3e0;
  }
  * { box-sizing: border-box; margin: 0; padding: 0; }
  html, body { width: 1200px; height: 900px; overflow: hidden; }
  body {
    background: var(--backdrop);
    font-family: "Open Sans", Arial, sans-serif;
    display: flex;
    flex-direction: column;
    align-items: center;
    justify-content: center;
    gap: 60px;
  }
  .card {
    position: relative;
    width: 630px;
    height: 360px;
    background: var(--card);
    box-shadow: 0 2px 10px rgba(0,0,0,0.12);
    overflow: hidden;
  }
  .brand {
    display: flex;
    align-items: center;
    gap: 12px;
    color: var(--green);
    font-weight: 600;
  }
  .brand-mark {
    width: 46px;
    height: 46px;
    background: var(--green);
    flex: none;
  }
  .brand-name { font-size: 30px; line-height: 1; letter-spacing: -0.5px; }
  .brand-tag { display: block; font-size: 13px; letter-spacing: 0.3px; margin-top: 4px; }

  /* back side */
  .card-back .brand { position: absolute; left: 48px; top: 44px; }
  .card-back .website {
    position: absolute; left: 48px; top: 110px;
    font-size: 12px; font-weight: 700; color: var(--green); letter-spacing: 1.2px;
  }
  .back-accent {
    position: absolute; right: -40px; bottom: -40px;
    width: 300px; height: 300px;
    background: var(--green-faint);
  }

  /* front side */
  .card-front .brand { position: absolute; left: 40px; top: 34px; }
  .holder { position: absolute; left: 40px; top: 112px; width: 380px; }
  .holder-name { font-size: 18px; font-weight: 700; color: var(--charcoal); letter-spacing: 1px; }
  .holder-title { font-size: 14px; font-weight: 600; color: var(--green); letter-spacing: 1px; margin-top: 2px; }
  .holder-rule { height: 1px; background: var(--rule); margin-top: 8px; width: 380px; }
  .address {
    position: absolute; left: 40px; top: 190px;
    font-size: 10.5px; color: var(--grey); line-height: 1.7; letter-spacing: 0.8px;
  }
  .contacts {
    position: absolute; left: 222px; top: 188px;
    list-style: none; font-size: 11px; color: var(--charcoal); letter-spacing: 0.8px;
  }
  .contacts li { display: flex; align-items: center; gap: 10px; height: 20px; }
  .contacts svg { width: 12px; height: 12px; fill: var(--green); flex: none; }
  .contacts .no-icon { padding-left: 22px; }
  .front-accent {
    position: absolute; right: 48px; bottom: 28px;
    width: 64px; height: 64px;
    background: var(--green);
  }
  .edge-band {
    position: absolute; left: 0; bottom: 0; width: 100%; height: 10px; background: var(--green);
  }
</style>
</head>
<body>

<section class="card card-back" aria-label="Business card, back">
  <div class="brand">
    <span class="brand-mark"></span>
    <span class="brand-name">Parkline<span class="brand-tag">Insurance Brokers</span></span>
  </div>
  <p class="website">www.parklineinsurance.com</p>
  <div class="back-accent" aria-hidden="true"></div>
</section>

<section class="card card-front" aria-label="Business card, front">
  <div class="brand">
    <span class="brand-mark"></span>
    <span class="brand-name">Parkline<span class="brand-tag">Insurance Brokers</span></span>
  </div>

  <div class="holder">
    <p class="holder-name">Daniel Moore, BA, CRM</p>
    <p class="holder-title">President &amp; CEO</p>
    <div class="holder-rule"></div>
  </div>

  <p class="address">4820 Maple Avenue NW<br>Calgary, AB &nbsp;T2R 0K5</p>

  <ul class="contacts">
    <li>
      <svg viewBox="0 0 24 24" aria-label="Phone"><path d="M6.6 10.8a15.1 15.1 0 0 0 6.6 6.6l2.2-2.2c.3-.3.7-.4 1-.2 1.1.4 2.3.6 3.6.6.6 0 1 .4 1 1V20c0 .6-.4 1-1 1A17 17 0 0 1 3 4c0-.6.4-1 1-1h3.5c.6 0 1 .4 1 1 0 1.3.2 2.5.6 3.6.1.3 0 .7-.2 1z"/></svg>
      555.010.1500
    </li>
    <li>
      <svg viewBox="0 0 24 24" aria-label="Mobile"><path d="M7 2h10a2 2 0 0 1 2 2v16a2 2 0 0 1-2 2H7a2 2 0 0 1-2-2V4a2 2 0 0 1 2-2zm0 3v13h10V5zm5 14.2a1 1 0 1 0 0 .1z"/></svg>
      555.010.9999
    </li>
    <li>
      <svg viewBox="0 0 24 24" aria-label="Fax"><path d="M6 2h10l2 2v5h2a2 2 0 0 1 2 2v7h-4v4H6v-4H2v-7a2 2 0 0 1 2-2h2zm2 2v5h8V5h-1V4zm0 11v5h8v-5z"/></svg>
      555.010.1700
    </li>
    <li class="no-icon">800.555.0148 Toll Free</li>
    <li>
      <svg viewBox="0 0 24 24" aria-label="Email"><path d="M3 5h18a1 1 0 0 1 1 1v12a1 1 0 0 1-1 1H3a1 1 0 0 1-1-1V6a1 1 0 0 1 1-1zm1 2.2V17h16V7.2l-8 5.3z M4.6 7 12 11.9 19.4 7z"/></svg>
      daniel@parklineinsurance.com
    </li>
  </ul>

  <div class="front-accent" aria-hidden="true"></div>
  <div class="edge-band"></div>
</section>

</body>
</html>
```